Junk Removal - Customers that are moving

junk collection business we want to gear this mailing to people who are moving and may need help in cleaning out the house for the open house or when the final move is near. Want to sound helpful and show it easier for us to do all the work

Target Market(s)

People Moving

Industry/Entity Type

House

Colors
3277b5
33a6d7

Requirements
Must have
• See attachment

```html
<!DOCTYPE html>
<html lang="en">
<head>
<meta charset="utf-8">
<title>Moving Cleanout Postcard</title>
<link rel="stylesheet" href="https://fonts.googleapis.com/css2?family=Oswald:wght@500;600&family=Source+Sans+3:wght@400;600;700;800&display=swap">
<style>
  :root {
    --brand-blue: #3277b5;
    --brand-deep: #1f5eae;
    --brand-sky: #33a6d7;
    --ink: #222;
    --grey: #8a8a8a;
    --line: #c9c9c9;
    --paper: #ffffff;
    --backdrop: #ecebe8;
  }
  * { box-sizing: border-box; margin: 0; padding: 0; }
  html, body { width: 918px; height: 1200px; overflow: hidden; }
  body {
    background: var(--backdrop);
    font-family: "Source Sans 3", Arial, sans-serif;
    color: var(--ink);
    position: relative;
  }
  .card {
    position: absolute;
    width: 692px;
    height: 537px;
    background: var(--paper);
    overflow: hidden;
    box-shadow: 0 2px 8px rgba(0,0,0,.18);
  }
  .card--front { left: 62px; top: 46px; }
  .card--back { left: 110px; top: 625px; }

  /* brand header */
  .brand { position: absolute; }
  .brand__tagline {
    font-family: "Oswald", "Arial Narrow", sans-serif;
    font-weight: 500;
    font-size: 15px;
    letter-spacing: .3px;
    color: var(--grey);
    white-space: nowrap;
  }
  .brand__tagline b { color: var(--ink); font-weight: 600; }
  .brand__name {
    font-family: "Source Sans 3", Arial, sans-serif;
    font-weight: 800;
    font-size: 44px;
    line-height: 1;
    color: var(--brand-deep);
    white-space: nowrap;
    margin-top: 3px;
  }
  .mascot {
    position: absolute;
    width: 72px;
    height: 118px;
    border-radius: 10px;
    background: linear-gradient(180deg, #7aa6d6 0%, #c9d7e6 55%, #b7bcc2 100%);
  }

  /* front */
  .photo-column { position: absolute; left: 0; top: 0; width: 264px; height: 537px; }
  .photo { position: absolute; left: 0; width: 264px; }
  .photo--scrap { top: 0; height: 172px; background: linear-gradient(135deg, #8d8a84, #5e5a55 45%, #b4aea6); }
  .photo--couch { top: 180px; height: 162px; background: linear-gradient(180deg, #b9b6ae 0%, #35406e 40%, #2b3460 70%, #a8a397 100%); }
  .photo--papers { top: 350px; height: 187px; background: linear-gradient(180deg, #d8d6d0, #a9a7a2 50%, #e0ded8); }

  .front-intro {
    position: absolute; left: 284px; top: 158px; width: 405px;
    font-size: 14.5px; line-height: 1.34; white-space: nowrap;
  }
  .front-intro p + p { margin-top: 6px; }

  .offer-band {
    position: absolute; left: 264px; top: 370px; width: 428px; height: 167px;
    background: linear-gradient(90deg, var(--brand-blue), var(--brand-deep));
  }
  .coupon {
    position: absolute; left: 294px; top: 262px; width: 420px; height: 144px;
    background: var(--brand-sky);
    border-radius: 72px 0 0 72px;
    box-shadow: 0 0 0 7px var(--paper);
    display: flex; align-items: center;
    padding-left: 30px;
    color: var(--paper);
  }
  .coupon__amount { display: flex; align-items: flex-start; font-weight: 600; }
  .coupon__currency { font-size: 34px; margin-top: 8px; }
  .coupon__value { font-size: 84px; line-height: 1; letter-spacing: -2px; }
  .coupon__copy { margin-left: 20px; }
  .coupon__title { font-size: 22px; font-weight: 600; }
  .coupon__sub { font-size: 18px; }

  .front-cta { position: absolute; left: 264px; top: 424px; width: 428px; text-align: center; color: var(--paper); }
  .front-cta__head { font-size: 26px; font-weight: 600; line-height: 1.1; }
  .front-cta__sub { font-size: 16px; font-weight: 700; margin-top: 2px; }
  .front-cta__url { font-size: 20px; letter-spacing: 4.5px; margin-top: 18px; }

  /* back */
  .back-headline { position: absolute; left: 24px; top: 156px; font-size: 15.5px; color: var(--brand-blue); font-weight: 600; }
  .benefits { position: absolute; left: 24px; top: 184px; width: 400px; }
  .benefits__title { font-size: 13px; font-weight: 700; margin-bottom: 3px; }
  .benefits__list { list-style: none; font-size: 10px; line-height: 1.35; }
  .benefits__list li { position: relative; padding-left: 17px; margin-bottom: 1px; }
  .benefits__list li::before {
    content: ""; position: absolute; left: 1px; top: 3px;
    width: 8px; height: 8px; border-radius: 50%; background: var(--brand-sky);
  }
  .benefits__list li::after {
    content: ""; position: absolute; left: 3.5px; top: 5px;
    width: 2px; height: 2px; border: solid var(--paper); border-width: 1.3px 1.3px 0 0;
    transform: rotate(45deg);
  }
  .back-footer {
    position: absolute; left: 0; top: 425px; width: 440px; height: 112px;
    background: linear-gradient(90deg, var(--brand-blue), var(--brand-deep));
    border-radius: 34px 0 0 0;
    color: var(--paper); text-align: center;
    padding-top: 20px;
  }
  .back-footer__info { font-size: 12.5px; }
  .back-footer__info b { font-weight: 700; }
  .back-footer__wish { font-size: 12.5px; margin-top: 9px; }
  .back-footer__sign { font-size: 19px; font-weight: 700; margin-top: 8px; }

  .stamp-box { position: absolute; left: 584px; top: 45px; width: 84px; height: 64px; border: 1.5px solid var(--line); }
  .address-lines { position: absolute; left: 485px; top: 206px; width: 180px; }
  .address-lines span { display: block; height: 1.5px; background: var(--line); margin-bottom: 32px; }
</style>
</head>
<body>

<section class="card card--front">
  <div class="photo-column">
    <div class="photo photo--scrap" role="img" aria-label="Photo of a heap of scrap metal and a broken shopping cart"></div>
    <div class="photo photo--couch" role="img" aria-label="Photo of a torn navy loveseat with foam showing"></div>
    <div class="photo photo--papers" role="img" aria-label="Photo of a stack of old newspapers"></div>
  </div>

  <div class="brand" style="left:282px; top:58px;">
    <div class="brand__tagline">SAFE, SECURE JUNK REMOVAL <b>1-800-555-0199</b></div>
    <div class="brand__name">1-800-CLEARIT</div>
  </div>
  <div class="mascot" style="left:606px; top:26px;" role="img" aria-label="Mascot illustration of a junk removal worker with a broom and trash can"></div>

  <div class="front-intro">
    <p>Dear Homeowner,</p>
    <p>Congratulations on your upcoming move!<br>We know how exciting and stressful moving your family and<br>all your belongings can be.</p>
  </div>

  <div class="offer-band"></div>
  <div class="coupon">
    <div class="coupon__amount"><span class="coupon__currency">$</span><span class="coupon__value">25</span></div>
    <div class="coupon__copy">
      <div class="coupon__title">DISCOUNT COUPON</div>
      <div class="coupon__sub">off any junk removal job!</div>
    </div>
  </div>

  <div class="front-cta">
    <div class="front-cta__head">Let 1-800-CLEARIT</div>
    <div class="front-cta__sub">help take some of the stress out of your move!</div>
    <div class="front-cta__url">www.1800clearit.com</div>
  </div>
</section>

<section class="card card--back">
  <div class="brand" style="left:24px; top:50px;">
    <div class="brand__tagline">SAFE, SECURE JUNK REMOVAL <b>1-800-555-0199</b></div>
    <div class="brand__name">1-800-CLEARIT</div>
  </div>
  <div class="mascot" style="left:350px; top:14px;" role="img" aria-label="Mascot illustration of a junk removal worker with a broom and trash can"></div>

  <h2 class="back-headline">Let 1-800-CLEARIT help take some of the stress out of your move!</h2>

  <div class="benefits">
    <h3 class="benefits__title">Here's how:</h3>
    <ul class="benefits__list">
      <li>No need to collect and remove unwanted items from the property; just point it out and we do all the work!</li>
      <li>No storage units or dumpsters to deal with, no physical work to worry about.</li>
      <li>We leave the areas from which we remove your unwanted "junk" "broom clean".</li>
      <li>Our up front price is not an estimate; the price we quote is the price you pay!</li>
      <li>We responsibly dispose of or recycle all items we remove.</li>
      <li>We are fully licensed (DEP #0051829) and insured.</li>
      <li>More than 75 years of family business behind all our work.</li>
      <li>Our services are ideal for both the initial cleanout of your for your open house or final cleanout days before moving 1-800CLEARIT (1-800-555-0199) is the one number to call.</li>
      <li>We remove all sorts of clutter including: Unwanted furniture, books, clothing, appliances, electronics, construction debris, carpeting, tile, mattresses, tires and much more!</li>
      <li>$25 DISCOUNT COUPON off any junk removal job!</li>
    </ul>
  </div>

  <div class="back-footer">
    <p class="back-footer__info">Visit our website <b>www.1800clearit.com</b> or give us a call for more information.</p>
    <p class="back-footer__wish">Wishing you the best of luck in your new home!</p>
    <p class="back-footer__sign">The 1-800 CLEARIT Team</p>
  </div>

  <div class="stamp-box"></div>
  <div class="address-lines"><span></span><span></span><span></span><span></span><span></span></div>
</section>

</body>
</html>
```